Brambel Logging Business Card Design Project

We need a new company business card. We provide professional timber harvesting (logging) and forest management services. I'm open to any creative design. Most company caps and shirts are navy blue and Light grey. Logo does not necessarily have to contain those colors. Logo containing picture of logging equipment, log truck, trees, or logs are acceptable. Be creative. Final logo should communicate our company's pride and professionalism in the East Texas Timber Industry.
Updates

Target Market(s)

Timber owners, sawmills, and forestry professionals

Industry/Entity Type

Business

Requirements
Must have
• Must have Contact Info.
Phone: 936-402-5817
address: PO Box 8462
Pine Hollow, Tx 77412
www.mbrambellogging.example
mbrambellogging@mailbox.example
Owner: Marv Brambel

Or design must leave room for this info.

```html
<!DOCTYPE html>
<html lang="en">
<head>
<meta charset="UTF-8">
<title>Brambel Logging – Business Card</title>
<link href="https://fonts.googleapis.com/css2?family=Lato:wght@400;700;900&display=swap" rel="stylesheet">
<style>
  :root {
    --navy: #3f3e93;
    --white: #ffffff;
    --grey-text: #8a8a8a;
    --rule: #333333;
    --backdrop: #e9e8ee;
  }
  * { margin: 0; padding: 0; box-sizing: border-box; }
  html, body { width: 1200px; height: 960px; overflow: hidden; }
  body {
    position: relative;
    background: var(--backdrop);
    font-family: "Lato", Arial, sans-serif;
    color: var(--white);
  }
  .card {
    position: absolute;
    left: 270px;
    width: 645px;
    height: 367px;
    box-shadow: 0 4px 12px rgba(0,0,0,0.25);
    overflow: hidden;
  }
  /* Front */
  .card-front { top: 84px; background: var(--navy); }
  .front-wordmark {
    position: absolute;
    top: 132px; left: 0; width: 100%;
    text-align: center;
    font-weight: 900;
    font-size: 52px;
    line-height: 1;
    color: var(--white);
  }
  .front-url {
    position: absolute;
    top: 222px; left: 0; width: 100%;
    text-align: center;
    font-size: 13px;
    letter-spacing: 1.6px;
    font-weight: 700;
  }
  /* Back */
  .card-back { top: 508px; background: var(--white); }
  .brand-row {
    position: absolute;
    top: 64px; left: 0; width: 100%;
    display: flex; align-items: center; justify-content: center;
  }
  .brand-name {
    font-weight: 900;
    font-size: 30px;
    color: var(--navy);
    padding-right: 18px;
  }
  .brand-divider { width: 2px; height: 55px; background: var(--rule); }
  .brand-tagline { padding-left: 18px; color: var(--grey-text); margin-top: -5px; }
  .brand-tagline .company { font-weight: 700; font-size: 21px; line-height: 28px; }
  .brand-tagline .slogan { font-weight: 400; font-size: 21px; line-height: 28px; }
  .contact-band {
    position: absolute;
    left: 0; top: 183px;
    width: 100%; height: 184px;
    background: var(--navy);
  }
  .owner { position: absolute; left: 111px; top: 74px; }
  .owner-name { font-weight: 700; font-size: 19px; line-height: 22px; }
  .owner-role { font-size: 14px; line-height: 16px; }
  .contact-details {
    position: absolute; left: 346px; top: 34px;
    font-size: 15px; line-height: 19px;
  }
  .address { margin-bottom: 20px; }
  .contact-line { display: flex; align-items: center; }
  .contact-line svg { width: 17px; height: 14px; margin-right: 8px; flex: none; }
</style>
</head>
<body>
  <section class="card card-front">
    <div class="front-wordmark">Brambel Logging</div>
    <div class="front-url">www.mbrambellogging.example</div>
  </section>

  <section class="card card-back">
    <div class="brand-row">
      <div class="brand-name">Brambel Logging</div>
      <div class="brand-divider"></div>
      <div class="brand-tagline">
        <div class="company">Company Name</div>
        <div class="slogan">Your Slogan</div>
      </div>
    </div>

    <div class="contact-band">
      <div class="owner">
        <div class="owner-name">Marv Brambel</div>
        <div class="owner-role">Owner</div>
      </div>
      <div class="contact-details">
        <div class="address">PO Box 8462<br>Pine Hollow, Tx 77412</div>
        <div class="contact-line">
          <svg viewBox="0 0 17 14" aria-hidden="true"><path d="M1 4 Q8.5 -1 16 4 L13 6 L11 4 H6 L4 6 Z M4 7 H13 L15 13 H2 Z" fill="#fff"/><circle cx="8.5" cy="10" r="1.8" fill="#3f3e93"/></svg>
          <span>936-402-5817</span>
        </div>
        <div class="contact-line">
          <svg viewBox="0 0 17 14" aria-hidden="true"><rect x="1" y="2" width="15" height="10" fill="none" stroke="#fff" stroke-width="1.5"/><path d="M1 2 L8.5 8 L16 2" fill="none" stroke="#fff" stroke-width="1.5"/></svg>
          <span>mbrambellogging@mailbox.example</span>
        </div>
        <div class="contact-line">
          <svg viewBox="0 0 17 14" aria-hidden="true"><rect x="1.5" y="1" width="14" height="9" fill="none" stroke="#fff" stroke-width="1.5"/><path d="M6 13 H11 M8.5 10 V13" stroke="#fff" stroke-width="1.5"/></svg>
          <span>www.mbrambellogging.example</span>
        </div>
      </div>
    </div>
  </section>
</body>
</html>
```